Ad Banner for knowledge management portal - Promote Knowledge Submission

This banner is used in knowledge management web site.

1. Banner size: 940x380
2. Business background: Provides maintenance, design and engineering, construction, machinery operation, material procurement and production management services for petrochemical and refinery business
3. We would like to see designs that
- Promote the benefits of sharing "Lesson Learned".
- Use the keyword "I will do it better if I have to do it again"
- Promote employees to submit "Lesson Learned". It is a lesson learned from work, submitted using a predefined form template.
- Promote a campaign that will give out souvenir for all employees who submit "Lesson Learned"
- Has the message "Click here to learn more about Lesson Learned"

Requirements
Must have
• Must have a picture of technician examining machine or equipments (using cartoon character)
Should not have
• Should not include picture of real people in the design

```html
<!DOCTYPE html>
<html lang="en">
<head>
<meta charset="utf-8">
<title>Lesson Learned – I will do it better if I have to do it again</title>
<link href="https://fonts.googleapis.com/css2?family=Open+Sans:wght@300;400;600;700&display=swap" rel="stylesheet">
<style>
  :root {
    --sky-blue: #1fb2ef;
    --paper: #ffffff;
    --paper-grey: #e6e7e9;
    --ink-white: #ffffff;
    --button-dark: #2e2e30;
    --button-darker: #151516;
    --button-edge: #5a5a5c;
    --quote-blue: #1fa3e6;
    --figure-orange: #e8873a;
    --figure-blue: #5cb8e6;
    --figure-brown: #a35a2c;
  }
  * { margin: 0; padding: 0; box-sizing: border-box; }
  html, body {
    width: 1200px;
    height: 485px;
    overflow: hidden;
    background: var(--paper);
  }
  .banner {
    position: relative;
    width: 1200px;
    height: 485px;
    overflow: hidden;
    font-family: "Open Sans", Arial, sans-serif;
    background: radial-gradient(ellipse at 85% 45%, var(--paper) 0%, #f3f3f4 45%, var(--paper-grey) 100%);
  }
  .banner__backdrop {
    position: absolute;
    inset: 0;
    width: 1200px;
    height: 485px;
  }
  .banner__copy {
    position: absolute;
    left: 89px;
    top: 152px;
    color: var(--ink-white);
    white-space: nowrap;
  }
  .banner__lead {
    font-weight: 700;
    font-size: 29px;
    line-height: 1;
    letter-spacing: -0.4px;
    text-shadow: 0 1px 2px rgba(0, 60, 110, 0.25);
  }
  .banner__headline {
    margin-top: 2px;
    font-weight: 300;
    font-size: 69px;
    line-height: 1;
    letter-spacing: -0.8px;
    text-shadow: 0 1px 2px rgba(0, 60, 110, 0.2);
  }
  .cta-primary {
    position: absolute;
    left: 89px;
    top: 301px;
    width: 334px;
    height: 60px;
    border-radius: 6px;
    border: 1px solid var(--button-edge);
    background: linear-gradient(to bottom, #4a4a4c 0%, var(--button-dark) 48%, var(--button-darker) 52%, #1e1e20 100%);
    box-shadow: 0 2px 4px rgba(0, 40, 80, 0.35);
    color: var(--ink-white);
    font-weight: 600;
    font-size: 33px;
    line-height: 57px;
    text-align: center;
    text-decoration: none;
    white-space: nowrap;
  }
  .cta-secondary {
    position: absolute;
    left: 442px;
    top: 329px;
    width: 126px;
    height: 31px;
    border-radius: 6px;
    background: var(--paper);
    color: var(--quote-blue);
    font-weight: 600;
    font-size: 18.5px;
    line-height: 31px;
    letter-spacing: -0.2px;
    text-align: center;
    text-decoration: none;
    white-space: nowrap;
  }
  .technician-figure {
    position: absolute;
    left: 790px;
    top: 18px;
    width: 320px;
    height: 460px;
    border-radius: 40px;
    background:
      radial-gradient(ellipse at 50% 18%, var(--figure-orange) 0%, rgba(232, 135, 58, 0.55) 22%, transparent 40%),
      radial-gradient(ellipse at 50% 55%, var(--figure-blue) 0%, rgba(92, 184, 230, 0.4) 25%, transparent 45%),
      radial-gradient(ellipse at 50% 82%, var(--figure-brown) 0%, rgba(163, 90, 44, 0.4) 25%, transparent 48%);
    opacity: 0.85;
  }
</style>
</head>
<body>
  <div class="banner">
    <svg class="banner__backdrop" viewBox="0 0 1200 485" aria-hidden="true">
      <defs>
        <linearGradient id="panelBlue" x1="0" y1="0" x2="1" y2="1">
          <stop offset="0" stop-color="#3ab8f2"/>
          <stop offset="0.55" stop-color="#1fb2ef"/>
          <stop offset="1" stop-color="#1aa6e6"/>
        </linearGradient>
        <radialGradient id="panelGlow" cx="0.2" cy="0.25" r="0.6">
          <stop offset="0" stop-color="#7fd6fa" stop-opacity="0.45"/>
          <stop offset="1" stop-color="#7fd6fa" stop-opacity="0"/>
        </radialGradient>
      </defs>
      <polygon points="0,0 696,0 731,485 0,485" fill="url(#panelBlue)"/>
      <polygon points="0,0 696,0 731,485 0,485" fill="url(#panelGlow)"/>
    </svg>

    <div class="banner__copy">
      <p class="banner__lead">Submit your Lesson Learned today and</p>
      <h1 class="banner__headline">get a cool souvenir</h1>
    </div>

    <a class="cta-primary" href="#" title="Click here to learn more about Lesson Learned" aria-label="Lesson Learned – click here to learn more about Lesson Learned">Lesson Learned</a>
    <a class="cta-secondary" href="#">Get Quote</a>

    <div class="technician-figure" role="img" aria-label="Cartoon technician in an orange hard hat and overalls holding a cordless drill, with a tool belt"></div>
  </div>
</body>
</html>
```